RW Business Card Design

My company provides advising/training and coaching services to business owners who want better financial results and better work/life balance. We help them through creating custom plans supported with education, strategic thinking and accountability.

We also help through some online courses which are geared to smaller businesses.
Updates

please also include our nth american contact # +1 555 208 4471

Industry/Entity Type

Financial

Contact Information for Business Card

Morgan Halberd
morgan@morganhalberd-example.com
+61 400 555 917
www.morganhalberd-example.com

```html
<!DOCTYPE html>
<html lang="en">
<head>
<meta charset="utf-8">
<title>RW Business Card</title>
<link rel="stylesheet" href="https://fonts.googleapis.com/css2?family=Arimo:ital,wght@1,700&family=Lato:wght@400;700&display=swap">
<style>
  :root {
    --bg: #e4e4e4;
    --card: #ffffff;
    --brand-blue: #4470b4;
    --slogan-blue: #2b4f9c;
    --swoosh-grey: #9a9a9a;
    --tagline-grey: #8a8a8a;
    --ink: #111111;
  }
  * { margin: 0; padding: 0; box-sizing: border-box; }
  html, body { width: 1200px; height: 900px; overflow: hidden; }
  body {
    background: var(--bg);
    font-family: "Lato", sans-serif;
    position: relative;
  }
  .card {
    position: absolute;
    width: 560px;
    height: 320px;
    background: var(--card);
    box-shadow: 0 6px 16px rgba(0,0,0,0.18);
    overflow: hidden;
  }
  .card--front { left: 70px; top: 90px; }
  .card--back { left: 570px; top: 490px; }

  .slogan {
    position: absolute;
    left: 0; right: 0; top: 62px;
    text-align: center;
    font-family: "Arimo", sans-serif;
    font-style: italic;
    font-weight: 700;
    font-size: 27px;
    line-height: 1.12;
    color: var(--slogan-blue);
  }

  .brand { position: absolute; white-space: nowrap; }
  .brand__lockup { display: flex; align-items: center; gap: 10px; }
  .brand__dot {
    width: 28px; height: 28px; border-radius: 50%;
    background: var(--brand-blue);
    flex: none;
  }
  .brand__name {
    font-family: "Lato", sans-serif;
    font-weight: 400;
    font-size: 20px;
    color: var(--brand-blue);
    line-height: 1;
  }
  .tagline {
    font-family: "Lato", sans-serif;
    font-size: 16px;
    color: var(--tagline-grey);
    margin-top: 6px;
    padding-left: 38px;
    line-height: 1;
  }
  .card--front .brand { left: 190px; top: 210px; }
  .card--back .brand { left: 300px; top: 36px; }

  .card__panel { position: absolute; inset: 0; }

  .holder-name {
    position: absolute;
    left: 40px; top: 176px;
    color: #ffffff;
    font-size: 18px;
    font-weight: 400;
    white-space: nowrap;
  }

  .contact {
    position: absolute;
    right: 22px; top: 196px;
    list-style: none;
    text-align: right;
  }
  .contact__item {
    display: flex;
    justify-content: flex-end;
    align-items: center;
    gap: 8px;
    font-size: 15.5px;
    font-weight: 700;
    color: var(--ink);
    line-height: 22px;
    white-space: nowrap;
  }
  .contact__item .note { font-weight: 400; }
  .contact__icon { width: 16px; height: 16px; flex: none; }
</style>
</head>
<body>

<section class="card card--front" aria-label="Business card front">
  <p class="slogan">Knowledge + Planning X Execution<br>=<br>Success</p>
  <div class="brand">
    <div class="brand__lockup">
      <span class="brand__dot"></span>
      <span class="brand__name">Morgan Halberd</span>
    </div>
    <p class="tagline">Clearer Plans, Stronger Results</p>
  </div>
</section>

<section class="card card--back" aria-label="Business card back">
  <svg class="card__panel" width="560" height="320" viewBox="0 0 560 320" aria-hidden="true">
    <rect width="560" height="320" fill="var(--brand-blue)"/>
    <path d="M250 0 C160 55 145 160 228 320 H560 V0 Z" fill="var(--swoosh-grey)"/>
    <path d="M274 0 C180 62 160 165 240 320 H560 V0 Z" fill="var(--card)"/>
  </svg>

  <div class="brand">
    <div class="brand__lockup">
      <span class="brand__dot"></span>
      <span class="brand__name">Morgan Halberd</span>
    </div>
    <p class="tagline">Clearer Plans, Stronger Results</p>
  </div>

  <p class="holder-name">Morgan Halberd</p>

  <ul class="contact">
    <li class="contact__item">+61 400 555 917
      <svg class="contact__icon" viewBox="0 0 16 16" aria-hidden="true"><path d="M2 6c0-2 3-3 6-3s6 1 6 3v1h-3V6H5v1H2z M4 8h8l1 5H3z" fill="var(--brand-blue)"/></svg>
    </li>
    <li class="contact__item"><span>+1 555 208 4471 <span class="note">(North America Office)</span></span>
      <svg class="contact__icon" viewBox="0 0 16 16" aria-hidden="true"><path d="M2 6c0-2 3-3 6-3s6 1 6 3v1h-3V6H5v1H2z M4 8h8l1 5H3z" fill="var(--brand-blue)"/></svg>
    </li>
    <li class="contact__item">morgan@morganhalberd-example.com
      <svg class="contact__icon" viewBox="0 0 16 16" aria-hidden="true"><rect x="1" y="3" width="14" height="10" fill="var(--brand-blue)"/><path d="M1 3l7 6 7-6" fill="none" stroke="#fff" stroke-width="1.2"/></svg>
    </li>
    <li class="contact__item">www.morganhalberd-example.com
      <svg class="contact__icon" viewBox="0 0 16 16" aria-hidden="true"><circle cx="8" cy="8" r="7" fill="var(--brand-blue)"/><path d="M1 8h14M8 1v14M3 4h10M3 12h10" stroke="#fff" stroke-width="0.9" fill="none"/><ellipse cx="8" cy="8" rx="3" ry="7" fill="none" stroke="#fff" stroke-width="0.9"/></svg>
    </li>
  </ul>
</section>

</body>
</html>
```